HML5 Web Application Design

We need a graphic design to give a HTML web application a modern look and feel. The design should be clean and neat with a metro inspired interface. All application uses vandrix controls so any experience with these would be great.
Perhaps you could also include a few screenshots of your previous work

Industry/Entity Type

Graphic Design

Requirements
Must have
• Must be HTML 5 compliant

```html
<!DOCTYPE html>
<html lang="en">
<head>
<meta charset="utf-8">
<title>clipforge – Login</title>
<link rel="stylesheet" href="https://fonts.googleapis.com/css2?family=Open+Sans:wght@300;400;600&display=swap">
<style>
  :root {
    --header-bg: #ffffff;
    --page-bg: #f4f4f4;
    --footer-bg: #e1e1e1;
    --brand-text: #1e1e1e;
    --brand-mark: #f2542d;
    --title-blue: #3a5fcf;
    --muted: #8a8a8a;
    --body-text: #333333;
    --placeholder: #a9a9a9;
    --field-border: #d0d0d0;
    --nav-bg: #eeeeee;
    --nav-text: #777777;
    --primary: #55b0d9;
    --primary-border: #3f98c2;
    --secondary-text: #999999;
  }
  * { box-sizing: border-box; margin: 0; padding: 0; }
  html, body { width: 1200px; height: 513px; overflow: hidden; }
  body {
    font-family: "Open Sans", "Segoe UI", sans-serif;
    font-weight: 300;
    background: var(--page-bg);
    position: relative;
  }
  .site-header {
    position: absolute; left: 0; top: 0; width: 1200px; height: 94px;
    background: var(--header-bg);
  }
  .brand {
    position: absolute; left: 70px; top: 32px;
    display: flex; align-items: center; gap: 10px;
  }
  .brand-mark { width: 32px; height: 32px; border-radius: 50%; background: var(--brand-mark); }
  .brand-name { font-size: 29px; font-weight: 400; color: var(--brand-text); letter-spacing: -0.3px; }
  .main-nav { position: absolute; top: 33px; left: 890px; display: flex; gap: 11px; }
  .nav-link {
    height: 36px; padding: 0 10px; line-height: 36px;
    background: var(--nav-bg); color: var(--nav-text);
    font-size: 14px; border-radius: 3px; text-decoration: none;
  }
  .login-panel { position: absolute; left: 67px; top: 104px; width: 380px; }
  .login-title { font-size: 44px; font-weight: 300; color: var(--title-blue); line-height: 54px; }
  .login-subtitle { font-size: 14px; color: var(--muted); margin-top: 4px; }
  .field {
    display: block; width: 365px; height: 46px; margin-top: 15px;
    border: 1px solid var(--field-border); background: var(--page-bg);
    font: 300 22px "Open Sans", sans-serif; color: var(--body-text); padding-left: 30px;
  }
  .field:first-of-type { margin-top: 36px; }
  .field::placeholder { color: var(--placeholder); }
  .form-row { position: relative; height: 38px; margin-top: 21px; }
  .remember { position: absolute; left: 3px; top: 12px; display: flex; align-items: center; gap: 9px; font-size: 16px; color: var(--body-text); }
  .checkbox { width: 21px; height: 21px; border: 1px solid #444; background: #fff; }
  .btn {
    position: absolute; left: 227px; width: 116px; height: 39px;
    font: 300 16px "Open Sans", sans-serif; text-align: center; line-height: 37px;
  }
  .btn-primary { top: 0; background: var(--primary); border: 1px solid var(--primary-border); color: #fff; }
  .signup-row { position: relative; height: 39px; margin-top: 31px; }
  .signup-row::before {
    content: ""; position: absolute; left: 0; top: 0; width: 375px; height: 1px;
    background: linear-gradient(90deg, transparent, #dcdcdc 20%, #dcdcdc 80%, transparent);
  }
  .signup-prompt { position: absolute; right: 176px; top: 10px; font-size: 16px; color: var(--body-text); white-space: nowrap; }
  .btn-secondary { top: 0; border: 1px solid var(--field-border); color: var(--secondary-text); background: var(--page-bg); }
  .site-footer {
    position: absolute; left: 0; top: 477px; width: 1200px; height: 36px;
    background: var(--footer-bg); font-size: 13px; color: var(--secondary-text);
    padding-left: 69px; line-height: 34px;
  }
</style>
</head>
<body>
  <header class="site-header">
    <div class="brand">
      <span class="brand-mark"></span>
      <span class="brand-name">clipforge</span>
    </div>
    <nav class="main-nav">
      <a class="nav-link" href="#">Register</a>
      <a class="nav-link" href="#">Log in</a>
      <a class="nav-link" href="#">Request Pin</a>
    </nav>
  </header>

  <main class="login-panel">
    <h1 class="login-title">Login</h1>
    <p class="login-subtitle">Use a local account to login</p>
    <form>
      <input class="field" type="text" placeholder="username">
      <input class="field" type="password" placeholder="password">
      <div class="form-row">
        <label class="remember"><span class="checkbox"></span>Remember me?</label>
        <button class="btn btn-primary" type="button">Login</button>
      </div>
      <div class="signup-row">
        <span class="signup-prompt">Don't have an account?</span>
        <button class="btn btn-secondary" type="button">Sign Up</button>
      </div>
    </form>
  </main>

  <footer class="site-footer">©2013 - KVE</footer>
</body>
</html>
```